Education / Investment Website Design (PDF Wireframe Provided)

More details are in the wireframe document

We need a website design for an investment education company. Our Clients purchase education courses through us. We use meridian toolkit (Wordpress) for our website. We just require the graphics in PSD (not coded) for the

1. Homepage - brightfunnelhub.com style
2. Blog page - brightfunnelhub.com style
3. Single Blog Post
4. Product page - Lernova.com style
5. Single Product Page - https://www.lernova.com/share-market-class-oceania/?ref=kP7qLmW3xT9Z
6. Contact Us Page (Contact Us Form, Map and Contact details)
7. About Us Page

See the attached Wireframe for the homepage

IMPORTANT
Websites we like are clean, white, similar to BrightFunnelHub.com and Lernova.com
Use of white space, big fonts, flat buttons

Attached wireframe is the flow of the homepage. (Homepage brief PDF)

Each section represents a "fold" as visitors are scrolling down. (Homepage showing folds PDF - how the visitor sees each section of the homepage as they scroll down the homepage)

We've got a clear idea of the elements on the page and looking for a great graphic / web designer to create those for us. (We do the coding)

Website currently is: southerncrosswealthschool.com.au (we want to simplify the website and have a more modern / flat design)

Questions: Please ask

Target Market(s)

Investors, People looking for Investment / Financial Education

Industry/Entity Type

Investment

Number of Pages Required

5+ page

Font styles to use
Sans Serif

Requirements
Must have
• Similar Items listed in the wireframe
• Clean Look - Flat design - elegant
• Roll-over (mouse on / mouse off) for Buttons and Top Banner Selection
Should not have
• Images that looks too much like "Stock Images"
• Please avoid bright orange

```html
<!DOCTYPE html>
<html lang="en">
<head>
<meta charset="utf-8">
<title>Southern Cross Wealth School — Home</title>
<link rel="stylesheet" href="https://fonts.googleapis.com/css2?family=Signika:wght@400;600&family=Roboto:wght@400;500;700&display=swap">
<style>
:root{
  --ink:#222428;
  --dark:#1e1f22;
  --blue:#1f3d9b;
  --blue-line:#2a55c9;
  --teal:#4cbfa6;
  --gray:#eeeeee;
  --gray-box:#d9d9d9;
  --muted:#777;
  --white:#fff;
  --footer:#2a2b2e;
  --footer-deep:#1b1c1e;
}
*{box-sizing:border-box;margin:0;padding:0}
html,body{width:1200px;height:4091px;overflow:hidden}
body{font-family:'Roboto',sans-serif;color:var(--ink);background:var(--white);position:relative}
.abs{position:absolute}
h1,h2,h3{font-family:'Signika',sans-serif;font-weight:400}

.topbar{left:0;top:0;width:1200px;height:44px;background:var(--dark);color:#ddd;font-size:14px}
.topbar p{position:absolute;left:112px;top:14px}
.topbar b{color:var(--teal);font-weight:400}
.search{position:absolute;left:882px;top:9px;width:206px;height:27px;border-radius:14px;background:#3a3b3f;color:#999;font-size:12px;padding:6px 14px}

.header{left:0;top:44px;width:1200px;height:76px;background:var(--white);border-bottom:1px solid #ddd}
.brand{position:absolute;left:112px;top:20px;display:flex;align-items:center;gap:10px}
.brand .dot{width:36px;height:36px;border-radius:50%;background:var(--ink)}
.brand span{font-family:'Signika',sans-serif;font-size:17px;line-height:18px;color:var(--ink);width:190px}
.nav{position:absolute;left:484px;top:31px;display:flex;gap:42px;font-size:13px;color:#333}
.nav .on{color:var(--blue-line)}
.nav-social{position:absolute;left:925px;top:33px;display:flex;gap:8px}
.nav-social i{width:11px;height:11px;background:#333;border-radius:50%}
.account{position:absolute;left:1040px;top:12px;font-size:11px;line-height:19px;text-align:right;width:48px;color:#333}

.hero{left:0;top:120px;width:1200px;height:530px;background:linear-gradient(135deg,#2c2d31,#1f2023)}
.hero h1{position:absolute;left:0;width:1200px;top:88px;text-align:center;color:#fff;font-size:46px;letter-spacing:1px}
.hero .sub{position:absolute;left:0;width:1200px;top:150px;text-align:center;color:#ddd;font-size:18px}
.choice{position:absolute;top:213px;width:218px;height:218px;border-radius:50%;border:4px solid var(--teal);background:#1b1c1f;color:#eee;text-align:center;font-size:13px;line-height:18px}
.choice.active{background:var(--teal);color:#1b1c1f;border-color:#2b9d86}
.choice svg{position:absolute;left:87px;top:48px}
.choice hr{position:absolute;left:38px;width:134px;top:110px;border:0;border-top:1px solid rgba(255,255,255,.4)}
.choice.active hr{border-top-color:rgba(0,0,0,.3)}
.choice p{position:absolute;left:32px;width:146px;top:122px}
.blue-line{left:0;top:648px;width:1200px;height:4px;background:var(--blue-line)}
.join{left:464px;top:627px;width:268px;height:48px;border-radius:24px;background:var(--blue);color:#fff;font-size:14px;text-align:center;line-height:48px}

.stats{left:0;top:676px;width:1200px;height:134px;background:var(--gray)}
.stat{position:absolute;top:22px;width:226px;height:88px;background:var(--gray-box);display:flex;align-items:center;padding-left:46px;gap:20px;font-size:16px;line-height:20px;color:#333}
.stat i{display:block;width:32px;height:32px;border-radius:6px}

.section-title{position:absolute;left:0;width:1200px;text-align:center;font-size:36px;color:var(--ink)}
.btn{position:absolute;background:var(--blue);color:#fff;text-align:center;font-size:16px;border-radius:3px}
.media{position:absolute}

.pricing{left:0;top:1514px;width:1200px;height:586px;background:var(--gray)}
.subtitle{position:absolute;left:0;width:1200px;text-align:center;font-size:16px}
.plan{position:absolute;top:131px;width:308px;height:392px;background:#fff;box-shadow:0 1px 4px rgba(0,0,0,.15)}
.plan h3{height:82px;background:linear-gradient(#3a3b3f,#202124);color:#fff;font-size:22px;text-align:center;line-height:82px}
.plan ul{list-style:none}
.plan li{height:47px;padding:0 18px;font-size:12.5px;display:flex;align-items:center;gap:10px;color:#333}
.plan li:nth-child(odd){background:#efefef}
.plan li .mark{color:var(--teal);font-weight:700;width:10px}
.plan .more{position:absolute;left:94px;top:335px;width:120px;height:34px;background:var(--blue);color:#fff;font-size:11px;text-align:center;line-height:34px;border-radius:3px}

.ask{left:0;top:2100px;width:1200px;height:646px;background:var(--teal)}

.quote{left:0;top:3130px;width:1200px;height:230px;background:#f1f1f1}
.quote .qmark{position:absolute;font-family:'Signika',sans-serif;font-size:60px;color:#444}
.quote p{position:absolute;left:160px;width:880px;top:76px;text-align:center;font-size:13px;line-height:24px;color:#666}
.quote .who{position:absolute;left:0;width:1200px;top:134px;text-align:center;font-size:12px;color:var(--blue-line)}
.dots{position:absolute;left:572px;top:184px;display:flex;gap:14px}
.dots i{width:9px;height:9px;border-radius:50%;background:#bfe6dc}
.dots i.on{background:var(--teal)}

.cta-band{left:0;top:3360px;width:1200px;height:103px;background:var(--dark);color:#fff;text-align:center;font-family:'Signika',sans-serif;font-size:36px;line-height:103px;letter-spacing:1px}
.cta-band b{color:var(--teal);font-weight:400}

.footer{left:0;top:3681px;width:1200px;height:344px;background:var(--footer);color:#bbb;font-size:12px}
.footer ul{position:absolute;top:32px;list-style:none;line-height:25px}
.footer h4{position:absolute;color:#fff;font-family:'Signika',sans-serif;font-weight:400;font-size:15px}
.footer .notice{position:absolute;left:112px;top:178px;width:976px;font-size:11px;line-height:20px;color:#999}
.footer .notice strong{display:block;color:#fff;font-weight:500;font-size:12px;margin-bottom:4px}
.footbar{left:0;top:4025px;width:1200px;height:66px;background:var(--footer-deep);color:#888;font-size:11px;line-height:66px;padding-left:112px}
</style>
</head>
<body>

<div class="abs topbar"><p>First time visitor? Then <b>start here</b> and <b>learn more</b> about Southern Cross Wealth School!</p><div class="search">Search...</div></div>

<header class="abs header">
  <div class="brand"><div class="dot"></div><span>SOUTHERN CROSS<br>Wealth School</span></div>
  <nav class="nav"><span class="on">HOME</span><span>BLOG</span><span>PRODUCTS</span><span>ABOUT US</span><span>MEMBERS</span></nav>
  <div class="nav-social"><i></i><i></i><i></i><i></i></div>
  <div class="account">Sign In<br>Join<br>About Us</div>
</header>

<section class="abs hero">
  <h1>EDUCATION. RECOMMENDATIONS. AUTOPILOT</h1>
  <p class="sub">Which investment service do you want to receive today?</p>
  <div class="choice" style="left:156px">
    <svg width="44" height="50" viewBox="0 0 44 50" fill="#fff"><rect x="6" y="4" width="4" height="34"/><path d="M0 34h16L8 46z"/><text x="22" y="20" font-size="16" font-family="Roboto">A</text><text x="22" y="42" font-size="16" font-family="Roboto">Z</text></svg>
    <hr><p>I want to learn to trade from A - Z</p>
  </div>
  <div class="choice active" style="left:491px">
    <svg width="44" height="44" viewBox="0 0 44 44" fill="#1b1c1f"><rect x="6" y="12" width="26" height="26"/><circle cx="19" cy="10" r="6"/><circle cx="34" cy="25" r="6"/></svg>
    <hr><p>I want to know exactly what local and US shares to Trade</p>
  </div>
  <div class="choice" style="left:824px">
    <svg width="44" height="44" viewBox="0 0 44 44" fill="#fff"><path d="M42 2L2 20l14 6 4 14 6-10 10 6z"/></svg>
    <hr><p>I want my Trading to be on Autopilot and outsource all the hard work</p>
  </div>
</section>
<div class="abs blue-line"></div>
<div class="abs join">Join Over 20,000 Fellow Investors</div>

<section class="abs stats">
  <div class="stat" style="left:110px"><i style="background:#3b5998"></i><span>2,00,000<br>Followers</span></div>
  <div class="stat" style="left:374px"><i style="background:#2aa3ef"></i><span>4,541<br>Followers</span></div>
  <div class="stat" style="left:636px"><svg width="34" height="26" viewBox="0 0 34 26"><rect width="34" height="26" rx="2" fill="#e07b1f"/><path d="M1 2l16 13L33 2" fill="none" stroke="#fff" stroke-width="2"/></svg><span>4,32,016<br>Subscribers</span></div>
  <div class="stat" style="left:854px"><i style="background:#4a9a3c;border-radius:50%"></i><span>8,819<br>Members</span></div>
</section>

<h2 class="section-title" style="top:850px">Trading and Investing Made Easy</h2>
<div class="media" role="img" aria-label="Explainer video still: busy trader juggling tasks, with play button" style="left:110px;top:925px;width:978px;height:447px;background:radial-gradient(circle at 50% 45%,#9fc3c7,#6e9fa5)"></div>
<div class="btn" style="left:434px;top:1415px;width:332px;height:60px;line-height:60px">New to Trading? Get Started Today</div>

<section class="abs pricing">
  <h2 class="section-title" style="top:36px">Trading and Investing Made Easy</h2>
  <p class="subtitle" style="top:88px">Select how you'd like to get started Today !</p>
  <div class="plan" style="left:110px"><h3>DO IT YOURSELF</h3><ul>
    <li><span class="mark">✓</span>Foundation of Trading and Investing</li>
    <li><span class="mark">✓</span>Options made easy</li>
    <li><span class="mark">✓</span>Futures and forex paymaster</li>
    <li><span class="mark">✓</span>Stock section masterclass</li>
    <li><span class="mark">✓</span>Mindset mastery</li></ul><div class="more">LEARN MORE</div></div>
  <div class="plan" style="left:445px"><h3>WE DO IT WITH YOU</h3><ul>
    <li><span class="mark">✓</span>Select an Education course</li>
    <li><span class="mark">+</span>Trade recommendations</li>
    <li><span class="mark">+</span>SMS and Email alerts</li>
    <li><span class="mark">+</span>Easy trade</li></ul><div class="more">LEARN MORE</div></div>
  <div class="plan" style="left:780px"><h3>WE DO IT FOR YOU</h3><ul>
    <li><span class="mark">✓</span>Select a Risk level</li>
    <li><span class="mark">✓</span>Select a strategy</li>
    <li><span class="mark">✓</span>Put your trading on autopilot</li></ul><div class="more">LEARN MORE</div></div>
</section>

<section class="abs ask">
  <h2 class="section-title" style="top:40px">Have a QUestion? We are here..., Ask Us anything</h2>
  <div class="media" role="img" aria-label="Illustration of advisors gathered around a circular target of arrows" style="left:110px;top:112px;width:978px;height:395px;background:radial-gradient(ellipse at 50% 55%,#cfeee8,#ffffff 70%)"></div>
  <div class="btn" style="left:415px;top:545px;width:370px;height:58px;line-height:58px">Book an Appointment with a Trading Coach</div>
</section>

<h2 class="section-title" style="top:2792px">Hear What Our SCWS Members are saying</h2>
<div class="media" role="img" aria-label="Video testimonial from a member in a suit" style="left:110px;top:2877px;width:308px;height:191px;background:linear-gradient(#8fa6b8,#4d5d6b)"></div>
<div class="media" role="img" aria-label="Video testimonial from a member with a laptop" style="left:445px;top:2877px;width:308px;height:191px;background:linear-gradient(#a7c4dc,#6f8ea8)"></div>
<div class="media" role="img" aria-label="Video testimonial from a member holding a tablet" style="left:780px;top:2877px;width:308px;height:191px;background:linear-gradient(#dcd6cc,#a69a8c)"></div>
<p class="abs" style="left:110px;width:308px;top:3082px;text-align:center;font-size:13px">Daniel Hart, <span style="color:var(--muted)">Location</span></p>
<p class="abs" style="left:445px;width:308px;top:3082px;text-align:center;font-size:13px">Lucy Marsh, <span style="color:var(--muted)">Location</span></p>
<p class="abs" style="left:780px;width:308px;top:3082px;text-align:center;font-size:13px">Nina Ford, <span style="color:var(--muted)">Location</span></p>

<section class="abs quote">
  <span class="qmark" style="left:136px;top:20px">“</span>
  <p>Our coaches explained every step in plain words, and within weeks I was placing my first trades with real confidence. The course structure, weekly sessions and member support made learning easy, and I now review my portfolio calmly each month.</p>
  <div class="who">Tara Quinn</div>
  <span class="qmark" style="left:1040px;top:90px">”</span>
  <div class="dots"><i class="on"></i><i></i><i></i></div>
</section>

<div class="abs cta-band">FIND OUT WHY THEY LOVE SCWS... <b>CLICK HERE »</b></div>

<div class="media" role="img" aria-label="eBook cover: guide to trading the share market" style="left:110px;top:3498px;width:176px;height:137px;background:linear-gradient(135deg,#2f6fa8,#173a5e)"></div>
<h3 class="abs" style="left:311px;top:3500px;font-size:24px">The 5 Critical Facts of Trading and Investing</h3>
<p class="abs" style="left:311px;top:3540px;font-size:16px;color:#444">Our most popular eBook</p>
<div class="btn" style="left:311px;top:3575px;width:254px;height:52px;line-height:52px">Click Here to Download Now</div>

<footer class="abs footer">
  <div class="brand" style="left:112px;top:28px"><div class="dot" style="background:#555"></div><span style="color:#fff">SOUTHERN CROSS<br>Wealth School</span></div>
  <p class="abs" style="left:112px;top:92px;width:220px;line-height:18px">SwiftTrade® is a registered trademark of Harbourline Charter Trading Ltd</p>
  <ul style="left:368px"><li>Links</li><li>Sign In</li><li>Join</li><li>Contact Us</li></ul>
  <ul style="left:491px"><li>Products</li><li>Options Made Easy</li><li>Futures and Forex Paymaster</li><li>Mindset Mastery</li></ul>
  <ul style="left:714px"><li>Other Links</li><li>Legal</li><li>Privacy Policy</li><li>FSG</li></ul>
  <h4 style="left:873px;top:30px">SOCIAL NETWORK</h4>
  <svg class="abs" style="left:873px;top:62px" width="130" height="30"><circle cx="14" cy="15" r="14" fill="#3b5998"/><circle cx="48" cy="15" r="14" fill="#2aa3ef"/><circle cx="82" cy="15" r="14" fill="#d34836"/><circle cx="116" cy="15" r="14" fill="#e8821e"/></svg>
  <div class="notice"><strong>CUSTOMER NOTICE</strong>SOUTHERN CROSS WEALTH SCHOOL PTY LTD is an authorised representative of CORAL COAST MARKETS ADVISORY PTY LTD and is authorised to provide general advice in securities and derivatives. No consideration has been given to your objectives, financial situation or needs. Any decision to invest or trade, and the method selected, is a personal decision and carries an inherent level of risk. You should seek independent advice on the suitability of this product for your circumstances. Please be aware that all trading activity is subject to both profit and loss and may not be suitable for you. Please click here to view the Financial Services Guide.</div>
</footer>
<div class="abs footbar">Southern Cross Wealth School Pty Ltd | Address: Tidewater House, Level 3, 48 Ocean Esplanade, Seacliff, QLD 4299 | Phone: 1300 555 018</div>

</body>
</html>
```